ZOVA Framework. the way you communicate in every situation and in all environments.

I would like you to create a diagram depicting a very specific process of communication. it must follow the look of the diagram that i have attached. this is going to be used in a book called BEDROCK. it is going to explain the fact that we communicate all the same way using this process as we communicate. it starts with the fact that everyone takes everything that is said personally and then moves on to filters, which is your own agenda or experience kicking in. then you move to your why it matters, which is your motivation and ends with the choice of words you use when you communicate. if you are going to be successful then you must separate the person from the issue.

Target Market(s)

market is executive business people around the world

Industry/Entity Type

Consulting

Font styles to use
Sans Serif

Colors

Designer to choose only greyscale colors for use in the design.

Requirements
Must have
• I would like it to have a diving/ocean/snorkel feel to it. The analogy we are using is to make a deep dive when you are communicating. it must have every part of the diagram you see, it starts at the top with the zova framework (and the words) it then connects to the filters which connects to the why it matters with connects to the words and then end with the separating the person from the issue.
Nice to have
• we are writing a black and white book NO color. therefore the words should be clear and easy to read. Each section should be able to stand on its own so we can write about it separately.
Should not have
• the diagram DOES NOT have to look like the one i gave you. it must explain the fact that it starts with ZOVA and ends with Separate and must pass through the three areas to get to the SEPARATE.

```html
<!DOCTYPE html>
<html lang="en">
<head>
<meta charset="utf-8">
<title>ZOVA Framework – Five Steps of Communication</title>
<link rel="stylesheet" href="https://fonts.googleapis.com/css2?family=Bebas+Neue&family=Fredoka:wght@600&family=Roboto:wght@400&display=swap">
<style>
  :root {
    --paper: #ffffff;
    --ink: #111111;
    --depth-1: #8a8a8a;
    --depth-1-deep: #6c6c6c;
    --depth-2: #5e5e5e;
    --depth-2-deep: #4c4c4c;
    --depth-3: #454545;
    --depth-3-deep: #353535;
    --depth-4: #2f2f2f;
    --depth-4-deep: #222222;
    --depth-5: #1c1c1c;
    --depth-5-deep: #0c0c0c;
    --ring-line: #ffffff;
    --bubble: #ffffff;
    --label: #ffffff;
  }
  * { box-sizing: border-box; margin: 0; padding: 0; }
  html, body {
    width: 1200px;
    height: 495px;
    overflow: hidden;
    background: var(--paper);
  }
  .diagram {
    position: relative;
    width: 1200px;
    height: 495px;
    background: var(--paper);
  }
  .diagram__title {
    position: absolute;
    top: 58px;
    left: 0;
    width: 100%;
    text-align: center;
    font-family: "Bebas Neue", "Arial Narrow", sans-serif;
    font-weight: 400;
    font-size: 40px;
    letter-spacing: 1px;
    color: var(--ink);
    line-height: 1;
  }
  .diagram__art {
    position: absolute;
    inset: 0;
  }
  .step {
    position: absolute;
    top: 226px;
    width: 150px;
    margin-left: -75px;
    text-align: center;
    color: var(--label);
  }
  .step__name {
    font-family: "Fredoka", "Arial Rounded MT Bold", sans-serif;
    font-weight: 600;
    font-size: 24px;
    line-height: 25px;
    letter-spacing: 0.5px;
    text-transform: uppercase;
  }
  .step__text {
    margin: 10px auto 0;
    width: 140px;
    font-family: "Roboto", Arial, sans-serif;
    font-size: 13.5px;
    line-height: 17px;
  }
  .step--1 { left: 156px; }
  .step--2 { left: 382px; }
  .step--3 { left: 606px; }
  .step--4 { left: 829px; }
  .step--5 { left: 1054px; }
  .step--1 .step__text { width: 128px; }
  .step--3 .step__text { width: 150px; }
</style>
</head>
<body>
<main class="diagram">
  <h1 class="diagram__title">5 Steps Diagram - Color Version- Vector Format</h1>

  <svg class="diagram__art" width="1200" height="495" viewBox="0 0 1200 495" aria-hidden="true">
    <defs>
      <linearGradient id="fill-depth-1" x1="0" y1="0" x2="0" y2="1">
        <stop offset="0" stop-color="var(--depth-1)"/>
        <stop offset="1" stop-color="var(--depth-1-deep)"/>
      </linearGradient>
      <linearGradient id="fill-depth-2" x1="0" y1="0" x2="0" y2="1">
        <stop offset="0" stop-color="var(--depth-2)"/>
        <stop offset="1" stop-color="var(--depth-2-deep)"/>
      </linearGradient>
      <linearGradient id="fill-depth-3" x1="0" y1="0" x2="0" y2="1">
        <stop offset="0" stop-color="var(--depth-3)"/>
        <stop offset="1" stop-color="var(--depth-3-deep)"/>
      </linearGradient>
      <linearGradient id="fill-depth-4" x1="0" y1="0" x2="0" y2="1">
        <stop offset="0" stop-color="var(--depth-4)"/>
        <stop offset="1" stop-color="var(--depth-4-deep)"/>
      </linearGradient>
      <linearGradient id="fill-depth-5" x1="0" y1="0" x2="0" y2="1">
        <stop offset="0" stop-color="var(--depth-5)"/>
        <stop offset="1" stop-color="var(--depth-5-deep)"/>
      </linearGradient>
    </defs>

    <g class="disc disc--1">
      <circle cx="156" cy="307" r="123" fill="url(#fill-depth-1)"/>
      <circle cx="156" cy="307" r="97" fill="none" stroke="var(--ring-line)" stroke-width="2.5"/>
    </g>

    <g class="disc disc--2">
      <circle cx="382" cy="307" r="123" fill="url(#fill-depth-2)"/>
      <circle cx="382" cy="307" r="97" fill="none" stroke="var(--ring-line)" stroke-width="2.5"/>
    </g>
    <g class="connector connector--1" fill="var(--depth-1)" stroke="var(--depth-1)">
      <path d="M301.4 387.6 A114 114 0 0 1 271.9 277.5" fill="none" stroke-width="12"/>
      <polygon points="276,257 259,282 287,280" stroke="none"/>
    </g>

    <g class="disc disc--3">
      <circle cx="606" cy="307" r="123" fill="url(#fill-depth-3)"/>
      <circle cx="606" cy="307" r="97" fill="none" stroke="var(--ring-line)" stroke-width="2.5"/>
    </g>
    <g class="connector connector--2" fill="var(--depth-2)" stroke="var(--depth-2)">
      <path d="M525.4 387.6 A114 114 0 0 1 495.9 277.5" fill="none" stroke-width="12"/>
      <polygon points="500,257 483,282 511,280" stroke="none"/>
    </g>

    <g class="disc disc--4">
      <circle cx="829" cy="307" r="123" fill="url(#fill-depth-4)"/>
      <circle cx="829" cy="307" r="97" fill="none" stroke="var(--ring-line)" stroke-width="2.5"/>
    </g>
    <g class="connector connector--3" fill="var(--depth-3)" stroke="var(--depth-3)">
      <path d="M748.4 387.6 A114 114 0 0 1 718.9 277.5" fill="none" stroke-width="12"/>
      <polygon points="723,257 706,282 734,280" stroke="none"/>
    </g>

    <g class="disc disc--5">
      <circle cx="1054" cy="307" r="123" fill="url(#fill-depth-5)"/>
      <circle cx="1054" cy="307" r="97" fill="none" stroke="var(--ring-line)" stroke-width="2.5"/>
    </g>
    <g class="connector connector--4" fill="var(--depth-4)" stroke="var(--depth-4)">
      <path d="M973.4 387.6 A114 114 0 0 1 943.9 277.5" fill="none" stroke-width="12"/>
      <polygon points="948,257 931,282 959,280" stroke="none"/>
    </g>
    <g class="connector connector--end" fill="var(--depth-5)" stroke="var(--depth-5)">
      <path d="M1134.6 387.6 A114 114 0 0 0 1164.1 277.5" fill="none" stroke-width="12"/>
      <polygon points="1160,257 1177,282 1149,280" stroke="none"/>
    </g>

    <g class="bubbles" fill="none" stroke="var(--bubble)" stroke-width="1.5">
      <circle cx="350" cy="222" r="3.5"/>
      <circle cx="357" cy="214" r="2.5"/>
      <circle cx="345" cy="213" r="2"/>
      <circle cx="814" cy="221" r="3.5"/>
      <circle cx="821" cy="213" r="2.5"/>
      <circle cx="829" cy="247" r="2.5"/>
      <circle cx="1085" cy="256" r="3.5"/>
      <circle cx="1092" cy="248" r="2.5"/>
    </g>
  </svg>

  <section class="step step--1">
    <h2 class="step__name">ZOVA<br>Framework</h2>
    <p class="step__text">When words are taken personally, what happens?</p>
  </section>

  <section class="step step--2">
    <h2 class="step__name">Your<br>Filters</h2>
    <p class="step__text">An accumulation of your experience, knowledge and values</p>
  </section>

  <section class="step step--3">
    <h2 class="step__name">Why it<br>Matters</h2>
    <p class="step__text">This is your compass. It is what motivattes you, what drive you.</p>
  </section>

  <section class="step step--4">
    <h2 class="step__name">Your<br>Words</h2>
    <p class="step__text">This is your immediate response, verbal or perhaps non-verbal</p>
  </section>

  <section class="step step--5">
    <h2 class="step__name">What<br>to do</h2>
    <p class="step__text">Separate the Person from the Issue</p>
  </section>
</main>
</body>
</html>
```